Brochure for a paper wholesaler who wants to educate his print industry clients

We will be making a stapled informative brochure, that contains basic information about our paper products - the types of paper there is, their characteristics and other useful information.
As we are part of a paper wholesaler group in Europe - VORENT, we received a brochure in German that has this kind of information. The text in it is not as important. What is important is the layout of the document and how the text will appear in it (added in the uploaded files - 210915_Wiessenswertes_TBLK_F51.pdf).
We are allowed to tinker with this file and adjust it to our needs. So there are also .idml and .indd files available (also in the uploaded files).
We would like to keep the custom page size of 210 x290mm (8.3x11.4 in), or you can go up to 210x297mm (8.3x11.7 in).
What we want is a modern looking design that contains our companies red bordo and white/ grey colours to replace the existing green colours in this borchure. The pictures and appearance of the file can be changed according to your views and what you think would look good. We don't necessarily want to keep the same design, we just want the layout of the document be the same, as we will be placing our translated text into it. The VORENT logo should be replaced with our own logo (KUMET Logo.png).
As for how it could look, it could go together with our paper presentation, for which the design can be seen in the "KUMET Base - v2.pptx".
Holiday season, so have a lot of tasks to take care of and not as much time to check ArtHarbor as often.

```html
<!DOCTYPE html>
<html lang="en">
<head>
<meta charset="utf-8">
<title>Worth Knowing – Brochure Presentation</title>
<link href="https://fonts.googleapis.com/css2?family=Montserrat:wght@400;500;600;700&family=Roboto+Condensed:wght@400;700&display=swap" rel="stylesheet">
<style>
:root{
  --bordo:#7b2a30;
  --bordo-deep:#5e1d22;
  --ink:#2a2a2a;
  --muted:#555;
  --board:#c8c8ca;
  --ghost:#a7a7a9;
  --paper:#ffffff;
  --cell:#ececec;
  --rule:#d6d6d6;
}
*{box-sizing:border-box}
html,body{margin:0;padding:0}
body{width:701px;height:1200px;overflow:hidden;background:var(--board);position:relative;font-family:'Montserrat',sans-serif;color:var(--ink)}

.board-title{position:absolute;top:22px;left:84px;width:540px;display:flex;justify-content:space-between;font-family:'Montserrat',sans-serif;font-weight:700;font-size:27px;color:var(--ghost);margin:0}

.brand-side{position:absolute;top:318px;font-family:'Montserrat',sans-serif;font-weight:500;font-size:13px;letter-spacing:9px;color:var(--bordo);display:flex;flex-direction:column;align-items:center;gap:14px}
.brand-side .mark-square{width:26px;height:26px;border:2px solid var(--bordo)}
.brand-left{left:108px}
.brand-right{left:512px}

/* cover */
.cover{position:absolute;left:235px;top:84px;width:230px;height:324px;background:var(--paper);box-shadow:0 3px 4px rgba(0,0,0,.28);overflow:hidden}
.cover-art{position:absolute;inset:0}
.cover-brand{position:absolute;left:13px;top:50px;font-weight:500;font-size:9px;letter-spacing:7px;color:var(--bordo)}
.cover-title{position:absolute;left:14px;top:222px;margin:0;font-family:'Roboto Condensed',sans-serif;font-weight:700;font-size:27px;line-height:.95;color:var(--bordo)}
.cover-sub{position:absolute;left:14px;top:282px;margin:0;font-family:'Roboto Condensed',sans-serif;font-size:9.4px;line-height:1.08;color:var(--ink)}

/* spreads */
.spread{position:absolute;width:296px;height:210px;display:flex;box-shadow:0 4px 4px rgba(0,0,0,.22)}
.page{width:148px;height:210px;position:relative;padding:9px 6px 0;font-size:2.1px;line-height:1.35;overflow:hidden}
.verso{background:linear-gradient(to right,#fff 82%,#ececec)}
.recto{background:linear-gradient(to right,#e8e8e8,#fff 16%)}
.page-foot{position:absolute;right:6px;bottom:5px;text-align:center}
.foot-name{font-size:3.4px;font-weight:600;color:var(--bordo);letter-spacing:.7px}
.foot-url{font-size:1.7px;color:var(--muted)}
h2{font-size:4.3px;color:var(--bordo);margin:0 0 3px;font-weight:600}
h3{font-size:2.3px;color:var(--bordo);margin:2px 0 1.4px;font-weight:600}
p{margin:0 0 1.4px}
.wave{position:absolute;left:0;bottom:0;width:100%;height:46px;background:linear-gradient(160deg,transparent 40%,#f1f1f1 70%,#fafafa)}

/* toc */
.toc{list-style:none;margin:8px 0 0;padding:0}
.toc li{display:flex;align-items:center;gap:3px;margin-bottom:6.3px}
.toc .toc-label{flex:1;border:.4px solid var(--muted);border-radius:3px;padding:.8px 3px;font-size:2.6px}
.toc .toc-num{width:11px;text-align:center;background:var(--bordo);color:#fff;border-radius:3px;font-size:2.4px;padding:.8px 0}

/* glossary */
.gloss{display:grid;grid-template-columns:28px 1fr;gap:2.2px 4px;font-size:1.9px;margin-bottom:5px}
.gloss dt{font-weight:600}
.gloss dd{margin:0}

.abbr{width:100%;border-collapse:collapse;font-size:1.8px}
.abbr td{padding:1.25px 2px;border-bottom:.3px solid rgba(255,255,255,.4)}
.abbr td:nth-child(1),.abbr td:nth-child(3){background:var(--bordo);color:#fff}
.abbr td:nth-child(2){background:#f4f4f4;width:34%}
.abbr td:nth-child(1){width:18%}

.data{width:100%;border-collapse:collapse;font-size:1.75px;text-align:center}
.data th{background:var(--bordo);color:#fff;font-weight:500;padding:1px .5px;border-right:.3px solid rgba(255,255,255,.5)}
.data td{padding:.85px .5px;border-bottom:.3px solid #fff}
.data tbody tr:nth-child(odd) td{background:var(--cell)}
.data td:first-child{font-weight:700}

.lists{display:flex;gap:14px;margin-top:4px;font-size:1.8px}
.lists ul{list-style:none;padding:0;margin:0;border-left:.4px solid var(--muted);padding-left:3px}
.lists li{margin-bottom:.9px}
.lists li b{display:inline-block;width:8px;font-weight:500}

.formula{display:flex;align-items:center;gap:3px;font-size:1.8px;margin:3px 0}
.formula .frac{text-align:center}
.formula .frac span{display:block;border-bottom:.3px solid var(--ink);padding-bottom:.6px;margin-bottom:.6px}

.rows{display:grid;grid-template-columns:24px 1fr;gap:2.2px 3px;font-size:1.8px}
.rows dt{font-weight:500}
.rows dd{margin:0}

.img-fill{border-radius:1px}
.tests{display:flex;gap:4px;margin:5px 0 2px}
.test{flex:1;text-align:center;font-size:1.7px}
.test .test-art{height:15px;border:.4px solid #999;background:linear-gradient(135deg,#f7f7f7,#d9d9d9);margin-bottom:1.5px}

.cert{position:relative;margin-bottom:5px;padding-right:14px}
.cert .badge{position:absolute;right:0;top:0;width:10px;height:10px;border-radius:2px;background:#3a8a4a}
.cert .badge.dark{background:#4a4a4a}
.cert .badge.blue{background:#2b5d9a;border-radius:50%}
</style>
</head>
<body>

<h1 class="board-title" aria-label="Translate"><span>T</span><span>R</span><span>A</span><span>N</span><span>S</span><span>L</span><span>A</span><span>T</span><span>E</span></h1>

<div class="brand-side brand-left"><span class="mark-square"></span>KUMET</div>
<div class="brand-side brand-right"><span class="mark-square"></span>KUMET</div>

<!-- Cover -->
<section class="cover">
  <svg class="cover-art" viewBox="0 0 230 324" preserveAspectRatio="none">
    <defs>
      <linearGradient id="crumple" x1="0" y1="0" x2="1" y2="1">
        <stop offset="0" stop-color="#3a3a3a"/><stop offset=".5" stop-color="#141414"/><stop offset="1" stop-color="#2c2c2c"/>
      </linearGradient>
      <linearGradient id="sheets" x1="0" y1="0" x2="1" y2="1">
        <stop offset="0" stop-color="#8e3a40"/><stop offset=".45" stop-color="#7b2a30"/><stop offset="1" stop-color="#5e1d22"/>
      </linearGradient>
      <linearGradient id="fold" x1="0" y1="0" x2="1" y2="0">
        <stop offset="0" stop-color="#e6e6e6"/><stop offset="1" stop-color="#fff"/>
      </linearGradient>
    </defs>
    <rect width="230" height="324" fill="#fff"/>
    <rect width="10" height="324" fill="url(#fold)"/>
    <path role="img" aria-label="Crumpled black paper texture" d="M150,0 L230,0 L230,102 C196,108 150,110 112,106 C124,66 138,30 150,0 Z" fill="url(#crumple)"/>
    <path d="M230,102 C200,120 190,160 200,190 C210,160 218,135 230,128 Z" fill="#d8d8d8"/>
    <path role="img" aria-label="Stack of bordo paper sheets fanned in a curve" d="M0,96 C70,84 150,100 230,182 L230,286 C190,210 110,150 0,168 Z" fill="url(#sheets)"/>
  </svg>
  <div class="cover-brand">KUMET</div>
  <h2 class="cover-title">WORTH<br>KNOWING!</h2>
  <p class="cover-sub">FORMATS, CLASSES<br>COLORS, CALCULATIONS</p>
</section>

<!-- Spread 1 -->
<section class="spread" style="left:41px;top:474px">
  <article class="page verso">
    <h2>TABLE OF CONTENTS</h2>
    <ol class="toc">
      <li><span class="toc-label">Technical Latin for advanced learners</span><span class="toc-num">03</span></li>
      <li><span class="toc-label">Cardboard at a glance</span><span class="toc-num">04</span></li>
      <li><span class="toc-label">The small 1x1 of the format school</span><span class="toc-num">04</span></li>
      <li><span class="toc-label">Extensive matter</span><span class="toc-num">05</span></li>
      <li><span class="toc-label">Help with weight problems</span><span class="toc-num">06</span></li>
      <li><span class="toc-label">The fine way to print</span><span class="toc-num">07</span></li>
      <li><span class="toc-label">Directional signpost</span><span class="toc-num">08</span></li>
      <li><span class="toc-label">Guaranteed colors</span><span class="toc-num">10</span></li>
      <li><span class="toc-label">For the sake of the environment, of course</span><span class="toc-num">10</span></li>
    </ol>
    <div class="wave"></div>
    <div class="page-foot"><div class="foot-name">KUMET</div><div class="foot-url">www.kumet-paper.example</div></div>
  </article>
  <article class="page recto">
    <h2>Technical Latin For Advanced Learners</h2>
    <h3>The Most Common Technical Terms And Abbreviations</h3>
    <dl class="gloss">
      <dt>uncoated</dt><dd>Unrefined, machine-smooth or satin papers made from various fibres can be produced</dd>
      <dt>satin/sharp satin</dt><dd>Papers smoothed afterwards in a calender and clearly polished</dd>
      <dt>painted</dt><dd>The surface of the paper is already coated in the paper machine or later in one coating machine. This results in a better print reproduction</dd>
      <dt>painted matt</dt><dd>The surface of the paper is matted in an additional step painted with pigments</dd>
      <dt>semi-matt painted</dt><dd>A special coating and calendering step creates a semi-matt surface</dd>
      <dt>painted glossy</dt><dd>Later satinizing and a special coat create a glossy surface</dd>
      <dt>FCO</dt><dd>Paper coated in the paper machine (inline) with a matt or glossy surface</dd>
    </dl>
    <h3>Abbreviations And Their Translation</h3>
    <table class="abbr">
      <tr><td>WFU</td><td>woodfree, uncoated</td><td>wood-free unpainted</td></tr>
      <tr><td>MFU</td><td>machine-finished special</td><td>woody, machine-smooth, uncoated</td></tr>
      <tr><td>WFC</td><td>woodfree, coated</td><td>painted wood-free</td></tr>
      <tr><td>MWC</td><td>middleweight, coated</td><td>double coated, woody, high degree of whiteness</td></tr>
      <tr><td>LWC</td><td>lightweight, coated</td><td>simply painted, containing wood</td></tr>
      <tr><td>ULWC</td><td>ultralightweight, coated</td><td>simply painted, wood, ultra-lightweight</td></tr>
      <tr><td>MFC</td><td>machine-finished, coated</td><td>machine-smooth painted, containing wood</td></tr>
      <tr><td>SC-A PLUS</td><td>supercalendered, bright</td><td>supercalendered, woody, high whiteness</td></tr>
      <tr><td>SC-A</td><td>supercalendered</td><td>supercalendered, woody, standard</td></tr>
      <tr><td>SC-B</td><td>softcalendered</td><td>soft-calendered, containing wood</td></tr>
      <tr><td>FCO</td><td>film coated offset</td><td>Paper coated in the paper machine (inline)</td></tr>
      <tr><td>HSWO</td><td>heatset web offset</td><td>Roller offset with hot air drying</td></tr>
    </table>
    <div class="page-foot"><div class="foot-name">KUMET</div><div class="foot-url">www.kumet-paper.example</div></div>
  </article>
</section>

<!-- Spread 2 -->
<section class="spread" style="left:364px;top:474px">
  <article class="page verso">
    <h2>Cardboard At A Glance</h2>
    <table class="data">
      <thead><tr><th></th><th></th><th>dash</th><th>Acquaintance Designation</th><th>Short name</th><th>Short name English</th></tr></thead>
      <tbody>
        <tr><td rowspan="2">Chromosulfate cardboard</td><td>Bleached, painted white</td><td>One-sided or two-sided painted</td><td>Sulfate pulp cardboard</td><td>GZ, deleted</td><td>SBS board</td></tr>
        <tr><td>Unbleached, brown</td><td>One-sided painted on both sides</td><td>Kraft cardboard</td><td>GN4, painted</td><td>CNK, coated board</td></tr>
        <tr><td rowspan="2">Chromo cardboard</td><td>With painted white back</td><td>Simply painted, front painted twice</td><td>Folding box cardboard</td><td>GC1, painted</td><td>FBB, folding box</td></tr>
        <tr><td>With uncoated bright back</td><td>Bright, uncoated back</td><td>Folding box cardboard</td><td>GC2, painted</td><td>FBB, manilla back</td></tr>
        <tr><td>Chromo duplex</td><td>With gray back</td><td>Back pigmented, front painted</td><td>Duplex cardboard</td><td>GD 2, painted</td><td>WLC, chipboard</td></tr>
      </tbody>
    </table>
    <h2 style="margin-top:5px">The Small 1x1 Of The Format School</h2>
    <h3>Sheet, Din And Storage Formats</h3>
    <p>Paper formats are standardized by norm. The original format of series A is a rectangle measuring 1 square meter.</p>
    <p>Each additional format is obtained by halving or doubling and has an aspect ratio of 1:√2. The series B, C and D are derived from series A. Raw formats match series A.</p>
    <div class="lists">
      <div><h3>DIN A FORMATS</h3><ul>
        <li><b>A0</b>841 x 1189 mm</li><li><b>A1</b>594 x 841 mm</li><li><b>A2</b>420 x 594 mm</li><li><b>A3</b>297 x 420 mm</li><li><b>A4</b>210 x 297 mm</li><li><b>A5</b>148 x 210 mm</li><li><b>A6</b>105 x 148 mm</li><li><b>A7</b>74 x 105 mm</li></ul></div>
      <div><h3>DIN B FORMATS</h3><ul>
        <li><b>B0</b>1000 x 1414 mm</li><li><b>B1</b>707 x 1000 mm</li><li><b>B2</b>500 x 707 mm</li><li><b>B3</b>353 x 500 mm</li><li><b>B4</b>250 x 353 mm</li><li><b>B5</b>176 x 250 mm</li><li><b>B6</b>125 x 176 mm</li><li><b>B7</b>88 x 125 mm</li></ul></div>
    </div>
    <div class="wave"></div>
    <div class="page-foot"><div class="foot-name">KUMET</div><div class="foot-url">www.kumet-paper.example</div></div>
  </article>
  <article class="page recto">
    <div style="display:flex;gap:16px">
      <div class="lists" style="margin:0"><div><h3>DIN C FORMATS</h3><ul>
        <li><b>C0</b>917 x 1297 mm</li><li><b>C1</b>648 x 917 mm</li><li><b>C2</b>458 x 648 mm</li><li><b>C3</b>324 x 458 mm</li><li><b>C4</b>229 x 324 mm</li><li><b>C5</b>162 x 229 mm</li><li><b>C6</b>114 x 162 mm</li></ul></div></div>
      <div class="lists" style="margin:0;flex-direction:column;gap:2px">
        <div><h3>DIN LONG</h3><ul><li><b>DL</b>220 x 110 mm</li></ul><p style="margin-top:1px">Envelope/mailer size</p></div>
        <div><h3>RAW FORMATS, UNCROPPED</h3><ul><li><b>A0</b>860 x 1120 mm</li><li><b>A1</b>610 x 860 mm</li><li><b>A2</b>430 x 610 mm</li><li><b>A3</b>305 x 430 mm</li></ul></div>
      </div>
    </div>
    <div class="img-fill" role="img" aria-label="Photo of a stack of paper sheets" style="position:absolute;right:4px;top:52px;width:40px;height:24px;background:linear-gradient(160deg,#f2f2f2,#9a9a9a 60%,#e0e0e0)"></div>
    <h2 style="margin-top:7px">Extensive Matter</h2>
    <table class="data">
      <thead><tr><th>Paper weight g/sqm</th><th>1.0x</th><th>1.3x</th><th>1.5x</th><th>1.8x</th><th>2.0x</th><th>2.2x</th><th>2.5x</th></tr></thead>
      <tbody>
        <tr><td>60</td><td>6,0</td><td>7,8</td><td>9,0</td><td>10,8</td><td>12,0</td><td>13,2</td><td>15,0</td></tr>
        <tr><td>70</td><td>7,0</td><td>9,1</td><td>10,5</td><td>12,6</td><td>14,0</td><td>15,4</td><td>17,5</td></tr>
        <tr><td>80</td><td>8,0</td><td>10,4</td><td>12,0</td><td>14,4</td><td>16,0</td><td>17,6</td><td>20,0</td></tr>
        <tr><td>90</td><td>9,0</td><td>11,7</td><td>13,5</td><td>16,2</td><td>18,0</td><td>19,8</td><td>22,5</td></tr>
        <tr><td>100</td><td>10,0</td><td>13,0</td><td>15,0</td><td>18,0</td><td>20,0</td><td>22,0</td><td>25,0</td></tr>
        <tr><td>110</td><td>11,0</td><td>14,3</td><td>16,5</td><td>19,8</td><td>22,0</td><td>24,2</td><td>27,5</td></tr>
        <tr><td>120</td><td>12,0</td><td>15,6</td><td>18,0</td><td>21,6</td><td>24,0</td><td>26,4</td><td>30,0</td></tr>
        <tr><td>135</td><td>13,5</td><td>17,6</td><td>20,3</td><td>24,3</td><td>27,0</td><td>29,7</td><td>33,8</td></tr>
        <tr><td>150</td><td>15,0</td><td>19,5</td><td>22,5</td><td>27,0</td><td>30,0</td><td>33,0</td><td>37,5</td></tr>
        <tr><td>170</td><td>17,0</td><td>22,1</td><td>25,5</td><td>30,6</td><td>34,0</td><td>37,4</td><td>42,5</td></tr>
        <tr><td>200</td><td>20,0</td><td>26,0</td><td>30,0</td><td>36,0</td><td>40,0</td><td>44,0</td><td>50,0</td></tr>
      </tbody>
    </table>
    <h3 style="color:var(--ink);margin-top:4px">Calculating the thickness of the book block (D)</h3>
    <div class="formula"><span>D (mm)=</span><div class="frac"><span>Number of sheets x weight per square meter (g/sqm) x volume of paper (1.x times)</span>1,000</div></div>
    <div class="page-foot"><div class="foot-name">KUMET</div><div class="foot-url">www.kumet-paper.example</div></div>
  </article>
</section>

<!-- Spread 3 -->
<section class="spread" style="left:41px;top:706px">
  <article class="page verso">
    <h2>Help With Weight Problems</h2>
    <table class="data">
      <thead><tr><th>Paper weight g/sqm</th><th>DIN A6</th><th>DIN long</th><th>DIN A5</th><th>DIN A4</th><th>DIN A3</th></tr></thead>
      <tbody>
        <tr><td>70</td><td>1,1 g</td><td>1,6 g</td><td>2,2 g</td><td>4,4 g</td><td>8,8 g</td></tr>
        <tr><td>80</td><td>1,3 g</td><td>1,7 g</td><td>2,5 g</td><td>5,0 g</td><td>10,0 g</td></tr>
        <tr><td>90</td><td>1,4 g</td><td>1,9 g</td><td>2,8 g</td><td>5,6 g</td><td>11,2 g</td></tr>
        <tr><td>100</td><td>1,6 g</td><td>2,1 g</td><td>3,2 g</td><td>6,3 g</td><td>12,5 g</td></tr>
        <tr><td>120</td><td>1,9 g</td><td>2,6 g</td><td>3,8 g</td><td>7,5 g</td><td>15,0 g</td></tr>
        <tr><td>150</td><td>2,4 g</td><td>3,2 g</td><td>4,7 g</td><td>9,4 g</td><td>18,7 g</td></tr>
        <tr><td>170</td><td>2,7 g</td><td>3,6 g</td><td>5,3 g</td><td>10,7 g</td><td>21,2 g</td></tr>
        <tr><td>200</td><td>3,1 g</td><td>4,2 g</td><td>6,2 g</td><td>12,5 g</td><td>25,0 g</td></tr>
      </tbody>
    </table>
    <h3 style="color:var(--ink);margin-top:5px">Calculating The Weight Of A Bow (G)</h3>
    <div class="formula"><span>G (g)=</span><div class="frac"><span>Length (mm) x width (mm) x weight per square meter (g/sqm)</span>1 000 000</div></div>
    <table class="data" style="margin-top:5px">
      <thead><tr><th>g/sqm</th><th>DIN C6</th><th>DIN long</th><th>DIN C6/5</th><th>Compact letter</th><th>DIN C5</th><th>DIN C4</th><th>Square</th></tr></thead>
      <tbody>
        <tr><td>60</td><td>2,8 g</td><td>3,6 g</td><td>3,9 g</td><td>4,4 g</td><td>5,6 g</td><td>11,1 g</td><td>7,3 g</td></tr>
        <tr><td>70</td><td>3,2 g</td><td>4,2 g</td><td>4,6 g</td><td>5,1 g</td><td>6,5 g</td><td>13,0 g</td><td>8,5 g</td></tr>
        <tr><td>75</td><td>3,5 g</td><td>4,5 g</td><td>4,9 g</td><td>5,5 g</td><td>7,0 g</td><td>13,9 g</td><td>9,1 g</td></tr>
        <tr><td>80</td><td>3,7 g</td><td>4,8 g</td><td>5,2 g</td><td>5,9 g</td><td>7,4 g</td><td>14,8 g</td><td>9,7 g</td></tr>
        <tr><td>90</td><td>4,2 g</td><td>5,5 g</td><td>5,9 g</td><td>6,6 g</td><td>8,4 g</td><td>16,7 g</td><td>10,9 g</td></tr>
        <tr><td>100</td><td>4,6 g</td><td>6,1 g</td><td>6,5 g</td><td>7,3 g</td><td>9,3 g</td><td>18,6 g</td><td>12,1 g</td></tr>
        <tr><td>110</td><td>5,1 g</td><td>6,7 g</td><td>7,2 g</td><td>8,1 g</td><td>10,2 g</td><td>20,4 g</td><td>13,3 g</td></tr>
      </tbody>
    </table>
    <div class="formula" style="margin-top:4px"><span>G (g)=</span><div class="frac"><span>Length (mm) x width (mm) x weight per square meter (g/sqm) x 2.5</span>1 000 000</div></div>
    <div class="page-foot"><div class="foot-name">KUMET</div><div class="foot-url">www.kumet-paper.example</div></div>
  </article>
  <article class="page recto">
    <div class="img-fill" role="img" aria-label="Photo of ink droplets splashed across white paper" style="position:absolute;right:0;top:4px;width:80px;height:22px;background:linear-gradient(100deg,#f5f5f5,#9c9c9c 45%,#e8e8e8)"></div>
    <h2>The fine way to print</h2>
    <h3 style="margin-top:7px">Processing instructions for fine papers</h3>
    <h3>Pressure</h3>
    <dl class="rows">
      <dt>Printing colors:</dt><dd>The color series recommended by the manufacturers for natural papers should be used</dd>
      <dt>Color order:</dt><dd>For single color machines: cyan, magenta, yellow, black. For two-color machines: cyan, magenta, black, yellow.</dd>
      <dt>Drying:</dt><dd>If the colors are removed, a longer drying time can be expected. Under normal conditions further processing is possible after 24 hours. The pH value of the wiping water is very important for drying, as is the ink film. Regular powdering prevents stacking, the grain should match the paper surface.</dd>
      <dt>Print provision:</dt><dd>By increasing the contact pressure between blanket and impression cylinder, an optimal printout is also ensured in recesses.</dd>
      <dt>Plucking:</dt><dd>Certain fine papers tend to pick, so colors with a high tack value should not be used. Anti-plucking agents help.</dd>
      <dt>Grid widths:</dt><dd>The surface quality of the paper is among other things crucial for the screen width. A finer 60 grid may be a good choice.</dd>
    </dl>
    <h3 style="margin-top:4px">Processing instructions for fine papers</h3>
    <h3>Finishing</h3>
    <dl class="rows">
      <dt>Paint:</dt><dd>Varnishes protect prints against mechanical influences and can create matt or glossy effects. Different techniques lead to different results and must be tested in advance. Full-surface varnishing is preferable to spot varnishing.</dd>
      <dt>Film lamination:</dt><dd>Due to their high quality and extraordinary colors, the finest papers are also impressive with their surface and the associated feel. If lamination is still necessary, tests are advised.</dd>
      <dt>Shape:</dt><dd>Blind or hot foil stamping is particularly suitable for stronger, voluminous and structured stamps. A test is definitely advisable.</dd>
      <dt>Further processing:</dt><dd>There are no particular restrictions on further processing for fine papers; however, care should be taken to fold in the direction of travel.</dd>
    </dl>
    <div class="page-foot"><div class="foot-name">KUMET</div><div class="foot-url">www.kumet-paper.example</div></div>
  </article>
</section>

<!-- Spread 4 -->
<section class="spread" style="left:364px;top:706px">
  <article class="page verso">
    <h2>Directional Signpost</h2>
    <h3>Test The Running Direction</h3>
    <p>Paper works – and now you can too. Paper is a natural product and therefore influenced by changes in air temperature or fluctuating humidity. The paper stretches or shrinks, which can affect printing or further processing. Fibres always move more towards their width, so it is worth knowing the direction of travel of the paper.</p>
    <p>Four examples of how you can quickly determine the direction of travel – without a lot of work.</p>
    <h3>1. Tear Test</h3>
    <p>If you tear a sheet from two sides, the tear will be parallel to the grain with less resistance and run straighter than the tear across it.</p>
    <h3>2. Bending Test</h3>
    <p>Cut a strip lengthwise and a second strip crosswise from a sheet and place both on top of each other. One strip will bend more easily; it shows the direction of travel.</p>
    <h3>3. Acid Test</h3>
    <p>If you pull two edges of a sheet between thumb and forefinger, one edge becomes wavy. Parallel to the smoother edge is the direction of travel.</p>
    <h3>4. Moisture Test</h3>
    <p>If you slightly moisten a section of paper on one side and place it wet side up, it will curl along the grain.</p>
    <div class="tests">
      <div class="test"><div class="test-art" role="img" aria-label="Drawing of the tear test"></div>1. TEAR TEST</div>
      <div class="test"><div class="test-art" role="img" aria-label="Drawing of the bending test"></div>2. BENDING TEST</div>
      <div class="test"><div class="test-art" role="img" aria-label="Drawing of the acid test"></div>3. ACID TEST</div>
      <div class="test"><div class="test-art" role="img" aria-label="Drawing of the moisture test"></div>4. MOISTURE TEST</div>
    </div>
    <div class="img-fill" role="img" aria-label="Photo of printed sheets spread on a table" style="position:absolute;left:8px;bottom:16px;width:105px;height:34px;background:linear-gradient(170deg,#fdfdfd,#bdbdbd 50%,#f4f4f4)"></div>
    <div class="page-foot"><div class="foot-name">KUMET</div><div class="foot-url">www.kumet-paper.example</div></div>
  </article>
  <article class="page recto">
    <div role="img" aria-label="Technical drawing showing how roll width and grain direction define long and short grain sheets in A formats" style="position:absolute;left:16px;top:19px;width:118px;height:168px;background:linear-gradient(180deg,#f1f1f1,#d9d9d9);border:.4px solid #9a9a9a"></div>
    <div class="page-foot"><div class="foot-name">KUMET</div><div class="foot-url">www.kumet-paper.example</div></div>
  </article>
</section>

<!-- Spread 5 -->
<section class="spread" style="left:202px;top:941px">
  <article class="page verso">
    <h2>Guaranteed Colors</h2>
    <h3>The Process Standard Offset (Sps) And The Current Standard</h3>
    <p>How can print and color quality be defined? How can deviations be proven? How is quality consistency ensured in print?</p>
    <p>The Standard Process Offset (SPS) provides answers to these questions and makes quality understandable, measurable and verifiable. It was sponsored by the printing association and the PRINTLAB institute to ensure standardized print production.</p>
    <p>The SPS includes specifications, methods, target and tolerance values for ensuring colour quality of reproduction through digital proof to offset printing. The aim is to make the division of labor in production as efficient as possible, optimize processes and avoid errors.</p>
    <p>One of the most important features of the SPS is the measurement of colors on the printing material. The color in interaction with paper is measured using a spectrophotometer and the color locus is determined. Deviation from the known color space is converted into a comparison value Delta E. The smaller the value, the better the printing result.</p>
    <p>The SPS also includes further guidelines already in place in pre-press with the adjustment of print data to the respective paper. Depending on the type of paper (coating, surface properties, etc.) you can print reproduce more or less intense colors.</p>
    <p>The SPS specifies working methods for the creation of color-accurate print documents. This is how it defines adaptation of image data to the paper class in CMYK in the form of profiles. There are also control wedges for proofing and gray control strips for printed sheets.</p>
    <h3>The Advantage For You</h3>
    <p>The offset process standard and the current version are intended to ensure that products printed in one city look the same as those printed in another.</p>
    <p>The SPS certificate assures your customer that their production partner produces consistent quality, achieved in a described workflow.</p>
    <h2 style="margin-top:4px">For The Sake Of The Environment, Of Course</h2>
    <p>The current status of environmentally certified products from the VORENT group can be found on the group website.</p>
    <div class="cert" style="padding-right:16px"><span class="badge blue" style="background:#6aa84f"></span>
      <h3>Loop To Loop Certified</h3>
      <p>The Loop to Loop product standard stipulates that materials and processing processes are classified into five categories: material health, recyclability, renewable energies and carbon management, responsible water use and social justice.</p>
    </div>
    <div class="img-fill" role="img" aria-label="Photo of printed colour proof sheets" style="position:absolute;left:14px;bottom:14px;width:100px;height:22px;background:linear-gradient(170deg,#f8f8f8,#c99a7c 45%,#efefef)"></div>
    <div class="page-foot"><div class="foot-name">KUMET</div><div class="foot-url">www.kumet-paper.example</div></div>
  </article>
  <article class="page recto">
    <div class="cert"><span class="badge dark"></span>
      <h3>WTC – Woodland Trust Council</h3>
      <p>Further information can be found at www.wtc-council.example</p>
      <p>The WTC was founded in response to a global conference on sustainable development. Forest owners, trade unions, representatives of indigenous groups in the timber industry and environmental associations stop ongoing global forest loss through independent certification. Certifiers check compliance with WTC rules in the forest and in the processing industry. Millions of hectares of forest in many countries are now certified.</p>
    </div>
    <div class="cert"><span class="badge"></span>
      <h3>FCPS – Program for Forest Certification Schemes</h3>
      <p>Further information can be found at www.fcps.example</p>
      <p>FCPS is the largest institution ensuring sustainable forest management through independent certification. Wood and wood products with the FCPS seal are proven to come from ecologically, economically and socially sustainable forestry. Thanks to its concept of regional certification, FCPS suits the structures of central forestry.</p>
    </div>
    <div class="cert"><span class="badge" style="background:#8fbf5a"></span>
      <h3>Continental Green Mark</h3>
      <p>Further information can be found at www.green-mark.example</p>
      <p>The Green Mark is the environmental label of the union and has been awarded to products and services since the nineties that have a lower environmental impact than comparable products. In the paper sector, certain limits apply for energy consumption, wastewater pollution and air emissions.</p>
    </div>
    <div class="cert"><span class="badge blue"></span>
      <h3>The Green Heron</h3>
      <p>Further information can be found at www.green-heron.example</p>
      <p>The Green Heron was awarded for the first time decades ago and is the oldest environmental label in the world. Independence and credibility are guaranteed by an environmental jury and the federal agencies. Only products that are particularly environmentally friendly and at the same time meet high standards are awarded. Recycled paper with the label has the goal of protecting resources.</p>
    </div>
    <div class="page-foot"><div class="foot-name">KUMET</div><div class="foot-url">www.kumet-paper.example</div></div>
  </article>
</section>

</body>
</html>
```